Ostrel Appraisals BV business cards (a financial services company)

I am looking for a business card design that stands out in the financial advisory field of business & intellectual property valuation. The business card design should be conservative, yet different. Address details have changed since the attached business card. New address is:

Molenvlietkade 27
4817 KT Leiden
The Netherlands

Telephone number remains the same.

```html
<!DOCTYPE html>
<html lang="en">
<head>
<meta charset="utf-8">
<title>Ostrel Appraisals BV — Business Cards</title>
<link href="https://fonts.googleapis.com/css2?family=Ubuntu:wght@400;700&display=swap" rel="stylesheet">
<style>
  :root {
    --backdrop: #3a3d42;
    --card-dark: #1f1f1f;
    --card-light: #ffffff;
    --ink-light: #ffffff;
    --ink-grey: #8a8a8a;
    --muted: #e6e6e6;
  }
  * { box-sizing: border-box; margin: 0; padding: 0; }
  html, body {
    width: 1200px; height: 1000px; overflow: hidden;
    background: var(--backdrop);
    font-family: "Ubuntu", sans-serif;
  }
  .sheet {
    position: relative; width: 1200px; height: 1000px;
  }
  .card {
    position: absolute; left: 220px; width: 760px; height: 434px;
    box-shadow: 0 10px 30px rgba(0,0,0,0.45);
    overflow: hidden;
  }
  .card--front {
    top: 50px; background: var(--card-dark);
    display: flex; align-items: center; justify-content: center;
  }
  .card--back { top: 516px; display: flex; }

  .brand-name {
    font-weight: 400; letter-spacing: 0.12em; text-transform: uppercase;
    font-size: 34px; color: var(--ink-light);
    display: flex; align-items: center; gap: 18px;
  }
  .brand-name__square {
    width: 22px; height: 22px; background: currentColor; flex: none;
  }
  .brand-name--on-light { color: var(--ink-grey); font-size: 26px; gap: 14px; }
  .brand-name--on-light .brand-name__square { width: 18px; height: 18px; }

  .back__brand {
    width: 46%; background: var(--card-light);
    display: flex; align-items: center; justify-content: center;
    padding-bottom: 60px;
  }
  .back__details {
    flex: 1; background: var(--card-dark); color: var(--ink-light);
    padding: 78px 46px 40px 20px; text-align: right;
  }
  .person__name { font-weight: 700; font-size: 22px; }
  .person__title { font-size: 17px; margin-top: 6px; color: var(--muted); }
  .address { font-size: 17px; line-height: 1.4; margin-top: 30px; color: var(--muted); }
  .contact { list-style: none; margin-top: 30px; font-size: 17px; color: var(--muted); }
  .contact li {
    display: flex; align-items: center; justify-content: flex-end; gap: 12px;
    line-height: 1.55;
  }
  .contact svg { width: 16px; height: 16px; flex: none; }
</style>
</head>
<body>
<main class="sheet">
  <section class="card card--front" aria-label="Card front">
    <div class="brand-name"><span class="brand-name__square"></span>Ostrel Appraisals</div>
  </section>

  <section class="card card--back" aria-label="Card back">
    <div class="back__brand">
      <div class="brand-name brand-name--on-light"><span class="brand-name__square"></span>Ostrel Appraisals</div>
    </div>
    <div class="back__details">
      <p class="person__name">Maarten Vos, CFA, ASA, RV</p>
      <p class="person__title">Managing Director</p>
      <p class="address">Molenvlietkade 27 4817 KT<br>Leiden The Netherlands</p>
      <ul class="contact">
        <li>+31 (0)70 384 1926
          <svg viewBox="0 0 16 16" aria-hidden="true"><path d="M4 1.5l2.2 2.6-1.3 1.6c.8 1.9 2.4 3.5 4.3 4.3l1.6-1.3 2.6 2.2-1.4 2.3C7 13 3 9 1.8 3z" fill="#fff"/></svg>
        </li>
        <li>mvos@ostrelappraisals.com
          <svg viewBox="0 0 16 16" aria-hidden="true"><rect x="1" y="3" width="14" height="10" fill="#fff"/><path d="M1.5 3.5L8 9l6.5-5.5" stroke="#1f1f1f" stroke-width="1.4" fill="none"/></svg>
        </li>
        <li>www.ostrelappraisals.com
          <svg viewBox="0 0 16 16" aria-hidden="true"><circle cx="8" cy="8" r="7" fill="#fff"/><ellipse cx="8" cy="8" rx="3" ry="7" stroke="#1f1f1f" fill="none"/><path d="M1 8h14" stroke="#1f1f1f"/></svg>
        </li>
      </ul>
    </div>
  </section>
</main>
</body>
</html>
```